Pitch Deck and business cards for Virtual Reality Startup

We need a redesign of our pitch deck to be funky, creative and interactive with animated graphics inline with our product (VR training)
Note: the design does not have to be orange that's just a template of the information we're sending you so we would like to see other colours also.

Target Market(s)

Investors

Industry/Entity Type

Media

Contact Information for Business Card

logo, Name, title, address, telephone, email, website

Font styles to use
Other font styles liked:
• funky but readable

Colors

Designer to choose colors to be used in the design.

Requirements
Must have
• Exciting non traditional design that fits a new, innovative, exciting and interactive technology
Nice to have
• .
Should not have
• traditional look and feel.

```html
<!DOCTYPE html>
<html lang="en">
<head>
<meta charset="utf-8">
<title>The problem – NEXA XR</title>
<link rel="stylesheet" href="https://fonts.googleapis.com/css2?family=Carlito:wght@400;700&display=swap">
<style>
  :root {
    --teal-deep: #3f9fb8;
    --teal-mid: #5fbfcc;
    --teal-light: #8ad6d6;
    --brush-dark: #5a4438;
    --brush-warm: #a07a62;
    --brush-light: #c9b3a2;
    --ink-logo: #2f2f33;
    --text-white: #ffffff;
    --accent-blue: #1b9cc0;
    --accent-blue-dark: #0f7fa3;
  }
  * { margin: 0; padding: 0; box-sizing: border-box; }
  html, body { width: 1200px; height: 676px; overflow: hidden; background: var(--teal-mid); }
  .slide {
    position: relative;
    width: 1200px;
    height: 676px;
    overflow: hidden;
    font-family: "Carlito", "Calibri", sans-serif;
  }
  .slide-backdrop {
    position: absolute;
    inset: 0;
    background:
      radial-gradient(ellipse at 20% 40%, rgba(40, 110, 140, 0.55), transparent 60%),
      linear-gradient(100deg, var(--teal-deep) 0%, var(--teal-mid) 45%, var(--teal-light) 100%);
  }
  .brush-band {
    position: absolute;
    left: 109px;
    top: 319px;
    width: 962px;
    height: 325px;
    border-radius: 40px 120px 60px 90px / 50px 70px 60px 80px;
    background:
      radial-gradient(ellipse at 65% 45%, rgba(220, 215, 205, 0.55), transparent 45%),
      linear-gradient(90deg, var(--brush-light) 0%, var(--brush-warm) 25%, var(--brush-dark) 55%, var(--brush-warm) 80%, var(--brush-light) 100%);
    opacity: 0.92;
  }
  .brand {
    position: absolute;
    left: 64px;
    top: 44px;
    display: flex;
    align-items: center;
    gap: 14px;
    font-weight: 700;
    font-size: 56px;
    letter-spacing: 4px;
    color: var(--ink-logo);
    line-height: 1;
  }
  .brand-mark {
    width: 14px;
    height: 14px;
    background: var(--ink-logo);
  }
  .headline-stack {
    position: absolute;
    left: 0;
    right: 0;
    text-align: center;
    color: var(--text-white);
    font-weight: 700;
    line-height: 1;
  }
  .section-title { top: 222px; font-size: 106px; }
  .problem-lead { top: 384px; font-size: 72px; }
  .problem-detail { top: 470px; font-size: 46px; }
  .problem-outcome {
    top: 508px;
    font-size: 138px;
    font-weight: 400;
    color: var(--accent-blue);
    -webkit-text-stroke: 3px var(--text-white);
    paint-order: stroke fill;
    text-shadow: 0 2px 0 var(--accent-blue-dark);
  }
</style>
</head>
<body>
  <main class="slide">
    <div class="slide-backdrop" role="img" aria-label="Photo of a person working on a laptop, washed in a teal overlay"></div>
    <div class="brush-band" role="img" aria-label="Brush-stroke window showing a close-up photo of hands on a laptop"></div>

    <div class="brand"><span>NEXA XR</span><span class="brand-mark"></span></div>

    <h1 class="headline-stack section-title">The problem</h1>
    <p class="headline-stack problem-lead">Traditional training</p>
    <p class="headline-stack problem-detail">does not prepare staff to be</p>
    <p class="headline-stack problem-outcome">Job Ready</p>
  </main>
</body>
</html>
```